Coastal Bright Sweep Business Card

We are a cleaning and waste management company with the slogan "making waste to landfill a thing of the past". We would like a re-design of our current business card. On the front we want to continue to use our logo as the focus point. On the back, we want the whole thing re-done to be less busy. We want the staff member’s name, the job title, mobile number, email and website. We do not want the address on the card. We still want the green, black and blue colours used, but a new font for the information on the back. Please do not change the logo design at all. We are also thinking about using icons to replace the text ‘mobile, email, website’. The “events + commercial” banner needs to be incorporated somewhere and needs to read “events + commercial + waste”. Another important point for consideration is that we are very concerned about being environmentally sustainable and will be printing on recycled paper. All designs should be made to compliment this in regards to boldness and colouring. Please find attached our logo, our colour chart and an image of our current business card.

```html
<!DOCTYPE html>
<html lang="en">
<head>
<meta charset="utf-8">
<title>Coastal Bright Sweep Business Card</title>
<link href="https://fonts.googleapis.com/css2?family=Open+Sans:wght@300;400;700&display=swap" rel="stylesheet">
<style>
  :root {
    --bg: #e9e6e1;
    --card: #ffffff;
    --card-front: #f4f4f2;
    --green: #7cc242;
    --green-dark: #5d9a2f;
    --blue: #36a9e1;
    --navy: #1f3f73;
    --ink: #333a40;
    --grey: #6d7379;
  }
  * { margin: 0; padding: 0; box-sizing: border-box; }
  html, body { width: 1200px; height: 800px; overflow: hidden; }
  body {
    background: var(--bg);
    font-family: "Open Sans", Arial, sans-serif;
    position: relative;
  }
  .card {
    position: absolute;
    top: 238px;
    width: 540px;
    height: 324px;
    border-radius: 18px;
    box-shadow: 0 6px 18px rgba(0,0,0,0.18);
    overflow: hidden;
  }
  .card-front { left: 40px; background: var(--card-front); }
  .card-back { left: 620px; background: var(--card); }

  .front-name {
    position: absolute;
    left: 0; right: 0; top: 50%;
    transform: translateY(-50%);
    text-align: center;
    font-weight: 700;
    font-size: 40px;
    line-height: 1.05;
    color: var(--green);
  }

  .staff-name {
    position: absolute;
    right: 36px; top: 30px;
    font-weight: 300;
    font-size: 26px;
    line-height: 1.2;
    color: var(--grey);
  }
  .staff-title {
    position: absolute;
    right: 36px; top: 66px;
    font-size: 13px;
    color: var(--navy);
  }
  .back-name {
    position: absolute;
    right: 36px; top: 150px;
    text-align: right;
    font-weight: 700;
    font-size: 26px;
    line-height: 1.05;
    color: var(--green);
  }
  .service-banner {
    position: absolute;
    right: 36px; top: 216px;
    font-size: 11px;
    letter-spacing: 0.06em;
    text-transform: uppercase;
    color: var(--blue);
  }

  .contact-rail {
    position: absolute;
    left: 26px; top: 120px; bottom: 0;
    width: 14px;
    background: var(--blue);
  }
  .contact-list { position: absolute; left: 14px; top: 146px; list-style: none; }
  .contact-row {
    height: 54px;
    display: flex;
    align-items: flex-start;
  }
  .contact-tab {
    width: 42px; height: 30px;
    background: var(--green);
    display: flex; align-items: center; justify-content: center;
    flex-shrink: 0;
  }
  .contact-tab svg { width: 16px; height: 16px; fill: var(--green-dark); }
  .contact-text {
    margin-left: 14px;
    font-size: 13px;
    color: var(--ink);
    line-height: 18px;
  }
  .contact-text::after {
    content: "";
    display: block;
    width: 64px; height: 2px;
    margin-top: 6px;
    background: var(--navy);
  }
</style>
</head>
<body>

<section class="card card-front">
  <div class="front-name">Coastal<br>Bright Sweep</div>
</section>

<section class="card card-back">
  <div class="staff-name">Morgan Ellery</div>
  <div class="staff-title">Client Manager</div>
  <div class="back-name">Coastal<br>Bright Sweep</div>
  <div class="service-banner">events + commercial + waste</div>

  <div class="contact-rail"></div>
  <ul class="contact-list">
    <li class="contact-row">
      <span class="contact-tab"><svg viewBox="0 0 16 16" aria-hidden="true"><path d="M4 1h3l1 4-2 1c1 2 2 3 4 4l1-2 4 1v3c0 1-1 2-2 2C7 14 2 9 2 3c0-1 1-2 2-2z"/></svg></span>
      <span class="contact-text">0400 555 218</span>
    </li>
    <li class="contact-row">
      <span class="contact-tab"><svg viewBox="0 0 16 16" aria-hidden="true"><path d="M1 3h14v10H1z M2 4l6 5 6-5" fill="none" stroke="#5d9a2f" stroke-width="1.6"/></svg></span>
      <span class="contact-text">mellery@coastalbrightsweep.com.au</span>
    </li>
    <li class="contact-row">
      <span class="contact-tab"><svg viewBox="0 0 16 16" aria-hidden="true"><g fill="none" stroke="#5d9a2f" stroke-width="1.4"><circle cx="8" cy="8" r="6.5"/><ellipse cx="8" cy="8" rx="3" ry="6.5"/><path d="M1.5 8h13M3 4.5h10M3 11.5h10"/></g></svg></span>
      <span class="contact-text">www.coastalbrightsweep.com.au</span>
    </li>
  </ul>
</section>

</body>
</html>
```